An anniversary gift for my girlfriend

My girlfriend and I have been dating for almost 2 years. We met online and this has afforded us the really unique opportunity to have the first words we said to each other (the whole conversation, in fact) preserved. We're moving in together in a few months and she doesn't know that I saved the conversation. I've been waiting for this to turn it into something we can hang in our new place.

The only phrase I want to use is:
"Well if you dislike people's knees then I think we'll get along famously"

It's an Nobody Leaves Before Midnight in Portland reference for the curious.

I want the poster to use the words themselves as the art; I'm thinking typography. I'd like it to match her aesthetic, she likes to wear Nora Vell and T. Brisk. Colors shouldn't be anything too "girly". Somewhere I'd like to include the date June 1, 2015. It shouldn't be a major piece of the poster though, just a way to denote the date.

It should fit (and be fully visible in) a 16x20 (inches) frame

Thanks in advance for the work!

Requirements
Must have
• Must use only the words: "Well if you dislike people's knees then I think we'll get along famously"
• I want this to be typography, so making the phrase the center of the poster and the art itself.

```html
<!DOCTYPE html>
<html lang="en">
<head>
<meta charset="utf-8">
<title>Famously — Anniversary Poster</title>
<link rel="stylesheet" href="https://fonts.googleapis.com/css2?family=Open+Sans:ital,wght@0,300;0,400;0,700;0,800;1,400;1,600;1,700;1,800&display=swap">
<style>
  :root {
    --backdrop: #e9e9eb;
    --paper: #ffffff;
    --ink: #111111;
    --heart-red: #e8262b;
    --heart-red-light: #f35a55;
    --lettering-grey: #2a2a2a;
  }
  html, body {
    margin: 0;
    padding: 0;
    width: 1200px;
    height: 900px;
    overflow: hidden;
    background: var(--backdrop);
  }
  .poster {
    position: absolute;
    left: 280px;
    top: 50px;
    width: 640px;
    height: 800px;
    background: var(--paper);
    box-shadow: 0 2px 10px rgba(0, 0, 0, 0.12);
    font-family: "Open Sans", "Helvetica Neue", Arial, sans-serif;
    color: var(--ink);
  }
  .phrase {
    position: absolute;
    top: 95px;
    left: 0;
    right: 0;
    margin: 0;
    text-align: center;
    font-size: 44px;
    line-height: 70px;
    font-weight: 400;
    letter-spacing: 0.02em;
  }
  .phrase .line { display: block; }
  .phrase .opener { font-weight: 700; font-style: italic; font-size: 38px; }
  .phrase .strong { font-weight: 700; }
  .phrase .light { font-weight: 300; }
  .phrase .heavy { font-weight: 800; letter-spacing: 0.03em; }
  .phrase .slanted { font-weight: 700; font-style: italic; }
  .finale {
    position: absolute;
    left: 5px;
    top: 450px;
    width: 620px;
    height: 210px;
  }
  .finale-art {
    position: absolute;
    inset: 0;
    width: 100%;
    height: 100%;
  }
  .finale-word {
    position: absolute;
    inset: 0;
    margin: 0;
    display: flex;
    align-items: center;
    justify-content: center;
    font-size: 72px;
    font-style: italic;
    font-weight: 700;
    letter-spacing: 0.01em;
    color: var(--ink);
  }
  .date {
    position: absolute;
    left: 0;
    right: 0;
    top: 718px;
    margin: 0;
    text-align: center;
    font-size: 18px;
    font-style: italic;
    font-weight: 400;
  }
</style>
</head>
<body>
  <main class="poster">
    <p class="phrase">
      <span class="line opener">Well</span>
      <span class="line">If <span class="strong">you</span> dislike</span>
      <span class="line">People's knees</span>
      <span class="line"><span class="light">then</span> <span class="heavy">I think</span></span>
      <span class="line"><span class="strong">We'll</span> <span class="slanted">get along</span></span>
    </p>
    <div class="finale">
      <svg class="finale-art" viewBox="0 0 620 210" preserveAspectRatio="none" role="img" aria-label="Hand-lettered word 'famously' in black brush script sweeping across a red painted heart">
        <defs>
          <linearGradient id="finale-tone" x1="0" y1="0" x2="1" y2="0">
            <stop offset="0" stop-color="var(--lettering-grey)" stop-opacity="0.12"/>
            <stop offset="0.5" stop-color="var(--heart-red-light)" stop-opacity="0.5"/>
            <stop offset="1" stop-color="var(--lettering-grey)" stop-opacity="0.12"/>
          </linearGradient>
        </defs>
        <rect x="0" y="0" width="620" height="210" rx="6" fill="url(#finale-tone)"/>
      </svg>
      <p class="finale-word">famously</p>
    </div>
    <p class="date">June 1, 2015</p>
  </main>
</body>
</html>
```